Business Card & Logo Design

Originally the brief was for a card only - I now think it's probably better to include a logo design as well. PLease add $200 to the Budget of $210, Apologies for the inconvenience for thaos that have already submitted designs.

Lamp And Harbor Studios Pty Ltd is a video/dvd/ production company. Primarily corporate medium to high end. It's a one man operation that's been in business 20 years.

The name " Lamp and Harbor" is a primarily a reference to Lucien Marbeck film that's about film making. Shooting "Lamp and harbor" is also a technique employed by cinematographers to make scenes shot in daylight look like night.

See the design emphasising blue day/night tones but open to other ideas.

Main Text can either be Lamp and Harbor Studios or Lamp And Harbor.
Updates

Many thanks to all designers who submitted ideas for this brief.

Choosing between the designs was very difficult indeed.

I wish everyone the best and may the next job be yours!

Walter

Industry/Entity Type

Business

Requirements
Must have
• Text for card:
In Larger Print
Lamp And Harbor Studios or Lamp And Harbor
Walter Brenic
In Smaller Print
Lamp And Harbor Studios Pty Ltd.
17 Calder Lane
Ashby Vale, VIC, 3188
P: 9734 2061
m: 0417 385 902
e: walterbrenic@examplemail.net

```html
<!DOCTYPE html>
<html lang="en">
<head>
<meta charset="utf-8">
<title>Lamp And Harbor Studios – Business Card</title>
<link rel="stylesheet" href="https://fonts.googleapis.com/css2?family=Mulish:wght@400;700;800;900&display=swap">
<style>
  :root {
    --stage: #3b3b3b;
    --card-blue: #0b4fde;
    --card-light: #e6e6e6;
    --ink-dark: #1a1a1a;
    --name-blue: #1a5fe6;
    --rule: #222222;
  }
  * { margin: 0; padding: 0; box-sizing: border-box; }
  html, body {
    width: 1200px; height: 351px; overflow: hidden;
    background: var(--stage);
    font-family: "Mulish", Arial, sans-serif;
  }
  .stage { position: relative; width: 1200px; height: 351px; }

  .card {
    position: absolute; top: 9px;
    width: 586px; height: 333px;
    border-radius: 21px; overflow: hidden;
  }
  .card--front { left: 9px; background: var(--card-blue); }
  .card--back  { left: 605px; background: var(--card-light); }

  .band { position: absolute; left: 0; width: 100%; }
  .card--front .band--light { top: 284px; height: 36px; background: var(--card-light); }
  .card--back .band--blue   { top: 285px; height: 35px; background: var(--card-blue); }

  .wordmark {
    position: absolute; text-align: center;
    font-weight: 900; text-transform: uppercase; line-height: 1;
    white-space: nowrap;
  }
  .wordmark__name { display: block; }
  .wordmark__sub  { display: block; }

  .card--front .wordmark {
    left: 0; width: 100%; top: 172px; color: var(--card-light);
  }
  .card--front .wordmark__name { font-size: 36px; letter-spacing: 1px; }
  .card--front .wordmark__sub  { font-size: 15px; letter-spacing: 2px; margin-top: 5px; }

  .card--back .wordmark {
    left: 62px; width: 224px; top: 161px; color: var(--card-blue);
  }
  .card--back .wordmark__name { font-size: 19px; }
  .card--back .wordmark__sub  { font-size: 10px; letter-spacing: 1.5px; margin-top: 4px; }

  .divider {
    position: absolute; left: 304px; top: 80px;
    width: 2px; height: 123px; background: var(--rule);
  }

  .contact { position: absolute; left: 319px; top: 79px; color: var(--ink-dark); }
  .contact__name { font-size: 22px; font-weight: 800; line-height: 1.1; }
  .contact__first { color: var(--name-blue); }
  .contact__company { font-size: 11px; font-weight: 700; margin-top: 4px; }
  .contact__details { list-style: none; margin-top: 10px; font-size: 12.5px; font-weight: 700; line-height: 15.5px; }
  .contact__label { color: var(--name-blue); display: inline-block; width: 18px; }
</style>
</head>
<body>
<div class="stage">
  <section class="card card--front">
    <div class="wordmark">
      <span class="wordmark__name">Lamp And Harbor</span>
      <span class="wordmark__sub">Studios</span>
    </div>
    <div class="band band--light"></div>
  </section>

  <section class="card card--back">
    <div class="wordmark">
      <span class="wordmark__name">Lamp And Harbor</span>
      <span class="wordmark__sub">Studios</span>
    </div>
    <div class="divider"></div>
    <div class="contact">
      <p class="contact__name"><span class="contact__first">Walter</span> Brenic</p>
      <p class="contact__company">Lamp And Harbor Studios Pty Ltd</p>
      <ul class="contact__details">
        <li>17 Calder Lane</li>
        <li>Ashby Vale, VIC, 3188</li>
        <li><span class="contact__label">p:</span>9734 2061</li>
        <li><span class="contact__label">m:</span>0417 385 902</li>
        <li><span class="contact__label">e:</span>walterbrenic@examplemail.net</li>
      </ul>
    </div>
    <div class="band band--blue"></div>
  </section>
</div>
</body>
</html>
```